Bramblecove Events Web Design Project

This is a bit of a challenging request. Bramblecove Events (event planning) and Orbit Party Rentals (event equipment rental), operate in the Northern Virginia area and we are in the process of marketing ourselves heavily as a "on stop celebration shop". Our customers range from large music festivals to smaller corporate functions. We are seeking to integrate two companies under one umbrella, our event planning company which also offers catering services " Bramblecove Event, LLC" with our event rental equipment company "Orbit Party Rentals." Both have new logos created through Sketch Harbor. I would like to have one portal that provides access to both companies and maintain the party rental URL as a stand alone to remain accessible to our loyal customers if possible. The only website that exist today is Orbit Party Rentals with the URL (www.orbitpartyhubzq.com), which needs a complete redesign, as it is very antiquated. This URL should still be able to stand on its own as well as integrated/accessible into the new overall parent company BRamblecove Events/ Our goal is to is to communicate to our customers that we are energetic, modern company with fresh celebration ideas and the hardware to go with it. There are numerous photos that need to be uploaded to the rental part of site. We will need to be able to update and make changes to photos without outside support.
Updates

Reason: I am changing the project to being a non-refundable and hope to get more submissions.

Target Market(s)

A very broad range of customers, from large rock festivals, to small country weddings and corporate functions

Industry/Entity Type

Event Planning

Requirements
Must have
• Must Have:
- - Ability to add and update photos without external support
-Modern interface ( look and feel)
-Easy user centered design
- multiple sections ( tabs) such as , Home, Event Planning, Catering, Galleries, Venues, Contact Us
Nice to have
• - ability to place event rental orders online

```html
<!DOCTYPE html>
<html lang="en">
<head>
<meta charset="utf-8">
<title>Orbit Party Rentals</title>
<link rel="stylesheet" href="https://fonts.googleapis.com/css2?family=Roboto:wght@300;400;500;700&display=swap">
<style>
  :root {
    --purple: #5a3e9e;
    --purple-dark: #4a2f8c;
    --orange: #f0702a;
    --grey-bg: #f2f2f2;
    --card-bg: #f3f3f3;
    --text: #777777;
    --white: #ffffff;
    --red: #d8232a;
  }
  * { box-sizing: border-box; margin: 0; padding: 0; }
  html, body { width: 1064px; height: 1200px; overflow: hidden; }
  body {
    position: relative;
    background: var(--white);
    font-family: 'Roboto', sans-serif;
    font-weight: 300;
    color: var(--text);
  }
  .abs { position: absolute; }

  /* Top bar */
  .top-bar { left: 0; top: 0; width: 1064px; height: 42px; background: var(--grey-bg); }
  .search { left: 788px; top: 9px; width: 161px; height: 25px; display: flex; }
  .search__field { flex: 1; background: var(--white); font-size: 8px; font-weight: 400; color: #777; padding: 8px 0 0 9px; letter-spacing: .3px; }
  .search__button { width: 25px; height: 25px; background: var(--purple); display: flex; align-items: center; justify-content: center; }

  /* Brand */
  .brand { left: 109px; top: 59px; display: flex; align-items: center; gap: 10px; }
  .brand__mark { width: 66px; height: 66px; border-radius: 50%; background: var(--purple); }
  .brand__name { font-size: 26px; font-weight: 700; color: var(--orange); line-height: 1; }

  /* Navigation */
  .main-nav { left: 421px; top: 94px; display: flex; gap: 24px; font-size: 17px; font-weight: 400; color: var(--purple); }
  .main-nav__item--active { position: relative; }
  .main-nav__caret { position: absolute; left: 28px; top: 21px; width: 0; height: 0; border-left: 5px solid transparent; border-right: 5px solid transparent; border-top: 7px solid var(--orange); }

  /* Hero */
  .hero {
    left: 106px; top: 140px; width: 853px; height: 357px;
    border: 1px solid #d6d6d6;
    background:
      linear-gradient(90deg, rgba(255,255,255,.92) 0%, rgba(255,255,255,.75) 32%, rgba(255,255,255,0) 55%),
      radial-gradient(circle at 62% 35%, #b9a7d8 0%, rgba(185,167,216,0) 22%),
      radial-gradient(circle at 46% 80%, #b8405a 0%, rgba(184,64,90,0) 14%),
      linear-gradient(160deg, #cfe6ee 0%, #d9d2c9 40%, #b9b1a6 70%, #e6e2dc 100%);
  }
  .hero__title { left: 21px; top: 148px; font-size: 29px; font-weight: 300; color: var(--purple); line-height: 37px; }
  .hero__arrow { top: 319px; width: 25px; height: 25px; border-radius: 50%; display: flex; align-items: center; justify-content: center; }
  .hero__arrow--prev { left: 29px; background: #3a3a3a; }
  .hero__arrow--next { left: 60px; background: var(--orange); }

  /* Dropdown */
  .dropdown { left: 553px; top: 126px; width: 179px; background: #f1f1f1; border: 1px solid #d8d8d8; box-shadow: 0 1px 3px rgba(0,0,0,.12); }
  .dropdown__item { height: 27.5px; padding: 0 11px; font-size: 11px; font-weight: 400; color: #666; display: flex; align-items: center; border-top: 1px solid #dedede; }
  .dropdown__item:first-child { border-top: none; font-size: 12.5px; }

  /* Welcome */
  .welcome__title { left: 0; width: 1064px; top: 523px; text-align: center; font-size: 16px; font-weight: 400; color: var(--purple); }
  .welcome__text { left: 113px; width: 838px; top: 568px; text-align: center; font-size: 12.5px; line-height: 21px; color: var(--text); }

  /* Cards */
  .card { top: 678px; width: 266px; height: 393px; background: var(--card-bg); border-radius: 8px; }
  .card__title { position: absolute; left: 20px; font-size: 16.5px; font-weight: 400; color: var(--purple); }
  .card__media { position: absolute; left: 20px; width: 226px; }
  .card__text { position: absolute; left: 21px; width: 230px; font-size: 12.5px; line-height: 21px; color: var(--text); }
  .card__link { position: absolute; left: 18px; font-size: 12.5px; font-weight: 400; color: var(--purple); }

  .video { top: 49px; height: 131px; background: linear-gradient(160deg, #4d6a3c 0%, #b4bda2 45%, #5f7648 100%); }
  .video__play { position: absolute; left: 91px; top: 35px; width: 37px; height: 37px; border-radius: 50%; background: rgba(30,30,30,.75); display: flex; align-items: center; justify-content: center; }
  .video__bar { position: absolute; left: 0; bottom: 0; width: 226px; height: 22px; background: #1e1e1e; }
  .video__track { position: absolute; left: 42px; top: 9px; width: 153px; height: 4px; border-radius: 2px; background: #555; }
  .video__fill { position: absolute; left: 0; top: 0; width: 40px; height: 4px; border-radius: 2px; background: #9aa; }

  .event-photo { top: 266px; height: 63px; background: linear-gradient(90deg, #3a2a6a 0%, #a78ad0 35%, #f1e6d0 50%, #8d6cc4 70%, #2d2450 100%); }

  .gallery-main { top: 50px; height: 143px; background: linear-gradient(180deg, #2f4f8f 0%, #6a8fc8 35%, #e8eef5 55%, #3e5a24 75%, #2b3a1a 100%); }
  .gallery-nav { position: absolute; top: 60px; width: 24px; height: 24px; border-radius: 50%; background: rgba(255,255,255,.85); display: flex; align-items: center; justify-content: center; }
  .thumbs { position: absolute; left: 20px; top: 212px; display: grid; grid-template-columns: repeat(3, 73px); gap: 5px 4px; }
  .thumb { height: 54px; }
  .thumb--1 { background: linear-gradient(160deg, #2a2670, #6f6fd6); }
  .thumb--2 { background: linear-gradient(160deg, #7a2b6e, #d8a3c8); }
  .thumb--3 { background: linear-gradient(180deg, #4f7dc8, #e8eef5 55%, #3f6e2a); }
  .thumb--4 { background: linear-gradient(160deg, #2a1a10, #c08a3e); }
  .thumb--5 { background: linear-gradient(160deg, #8a1f7a, #e05bb0); }
  .thumb--6 { background: linear-gradient(160deg, #d9d2c9, #8a7460); }
  .follow { position: absolute; left: 62px; top: 349px; width: 139px; height: 23px; background: var(--red); border-radius: 4px; color: var(--white); font-size: 10px; font-weight: 700; display: flex; align-items: center; justify-content: center; gap: 4px; letter-spacing: .2px; }
  .follow__name { font-weight: 700; font-size: 12px; }

  .catering-photo { top: 60px; height: 142px; left: 19px; width: 228px; background: linear-gradient(160deg, #5a6f5a 0%, #d9824a 35%, #c8b49a 60%, #8a8a8a 100%); }

  /* Footer */
  .footer { left: 0; top: 1100px; width: 1064px; height: 100px; background: #efefef; }
  .footer__links { left: 113px; top: 34px; display: flex; font-size: 12.5px; font-weight: 400; color: var(--purple); }
  .footer__links span.sep { color: #999; margin: 0 9px; }
  .footer__legal { left: 116px; top: 67px; display: flex; font-size: 12.5px; font-weight: 400; color: var(--purple); }
  .footer__legal span.sep { color: #999; margin: 0 9px; }
  .partner { left: 665px; top: 40px; display: flex; align-items: center; gap: 6px; font-size: 15px; font-weight: 500; color: var(--purple); }
  .partner__dot { width: 14px; height: 14px; border-radius: 50%; background: var(--orange); }
  .social { left: 822px; top: 36px; display: flex; gap: 5px; }
  .social__item { width: 28px; height: 28px; border-radius: 50%; }
  .social__item--a { background: #3b5998; }
  .social__item--b { background: #f7931e; }
  .social__item--c { background: #29a9e0; }
  .social__item--d { background: #e32b2b; }
</style>
</head>
<body>

  <header>
    <div class="abs top-bar"></div>
    <form class="abs search" role="search">
      <div class="search__field">SEARCH</div>
      <div class="search__button">
        <svg width="10" height="10" viewBox="0 0 10 10"><circle cx="4" cy="4" r="2.6" fill="none" stroke="#fff" stroke-width="1.4"/><line x1="6" y1="6" x2="8.6" y2="8.6" stroke="#fff" stroke-width="1.6"/></svg>
      </div>
    </form>

    <div class="abs brand">
      <div class="brand__mark"></div>
      <div class="brand__name">Orbit Party Rentals</div>
    </div>

    <nav class="abs main-nav">
      <span>Home</span>
      <span>Portfolio</span>
      <span class="main-nav__item--active">Services<i class="main-nav__caret"></i></span>
      <span>Planning Tools</span>
      <span>About Us</span>
      <span>Contact Us</span>
    </nav>
  </header>

  <section class="abs hero" role="img" aria-label="Photo of an elegant banquet table with candles, glassware and purple flower centrepieces">
    <h1 class="abs hero__title">Serving Northern Virginia<br>Party Needs Since 1999!</h1>
    <div class="abs hero__arrow hero__arrow--prev">
      <svg width="10" height="12" viewBox="0 0 10 12"><polyline points="7,1 2,6 7,11" fill="none" stroke="#fff" stroke-width="2.2"/></svg>
    </div>
    <div class="abs hero__arrow hero__arrow--next">
      <svg width="10" height="12" viewBox="0 0 10 12"><polyline points="3,1 8,6 3,11" fill="none" stroke="#fff" stroke-width="2.2"/></svg>
    </div>
  </section>

  <ul class="abs dropdown">
    <li class="dropdown__item">Products</li>
    <li class="dropdown__item">Emergency &amp; Long Term Rentals</li>
    <li class="dropdown__item">Event Planning</li>
    <li class="dropdown__item">Catering</li>
  </ul>

  <section>
    <h2 class="abs welcome__title">Welcome To Orbit Party Rentals</h2>
    <p class="abs welcome__text">Sed ut perspiciatis unde omnis iste natus error sit voluptatem accusantium doloremque laudantium, totam rem aperiam, eaque ipsa quae ab illo inventore veritatis et quasi architecto beatae vitae dicta sunt explicabo. Nemo enim ipsam voluptatem quia voluptas sit aspernatur aut odit aut fugit, sed quia consequuntur magni dolores eos qui ratione voluptatem sequi nesciunt.</p>
  </section>

  <article class="abs card" style="left:115px;">
    <h3 class="card__title" style="top:24px;">How It works</h3>
    <div class="card__media video" role="img" aria-label="Video still of guests raising glasses in a toast outdoors">
      <div class="video__play"><svg width="12" height="12" viewBox="0 0 12 12"><polygon points="3,1 11,6 3,11" fill="#fff"/></svg></div>
      <div class="video__bar">
        <svg style="position:absolute;left:12px;top:7px" width="8" height="8" viewBox="0 0 8 8"><rect x="0" y="0" width="3" height="8" fill="#fff"/><rect x="5" y="0" width="3" height="8" fill="#fff"/></svg>
        <div class="video__track"><div class="video__fill"></div></div>
        <svg style="position:absolute;left:206px;top:7px" width="10" height="8" viewBox="0 0 10 8"><polygon points="0,2.5 3,2.5 6,0 6,8 3,5.5 0,5.5" fill="#fff"/><path d="M7.5 2 Q9 4 7.5 6" fill="none" stroke="#fff"/></svg>
      </div>
    </div>
    <span class="card__link" style="top:196px;">Rental Orders Online &gt;&gt;</span>
    <h3 class="card__title" style="top:236px; left:18px;">Event Planning</h3>
    <div class="card__media event-photo" role="img" aria-label="Photo of a banquet hall lit in purple with a chandelier"></div>
    <p class="card__text" style="top:342px;">Lorem Ipsum is simply dummy text of the printing and typesetting industry..</p>
  </article>

  <article class="abs card" style="left:398px;">
    <h3 class="card__title" style="top:22px;">Photo Gallery</h3>
    <div class="card__media gallery-main" role="img" aria-label="Photo of a large white event tent on a lawn at dusk">
      <div class="gallery-nav" style="left:9px;"><svg width="8" height="10" viewBox="0 0 8 10"><polyline points="6,1 2,5 6,9" fill="none" stroke="#333" stroke-width="2"/></svg></div>
      <div class="gallery-nav" style="left:193px;"><svg width="8" height="10" viewBox="0 0 8 10"><polyline points="2,1 6,5 2,9" fill="none" stroke="#333" stroke-width="2"/></svg></div>
    </div>
    <div class="thumbs">
      <div class="thumb thumb--1" role="img" aria-label="Dance floor with purple lighting"></div>
      <div class="thumb thumb--2" role="img" aria-label="Reception hall in magenta light"></div>
      <div class="thumb thumb--3" role="img" aria-label="White peaked tents outdoors"></div>
      <div class="thumb thumb--4" role="img" aria-label="Evening stage with warm lights"></div>
      <div class="thumb thumb--5" role="img" aria-label="Tent interior in pink light"></div>
      <div class="thumb thumb--6" role="img" aria-label="Dining tables set for a banquet"></div>
    </div>
    <div class="follow">FOLLOW ME ON <span class="follow__name">Pinvault</span></div>
  </article>

  <article class="abs card" style="left:683px; top:674px; height:392px;">
    <h3 class="card__title" style="top:30px;">Catering</h3>
    <div class="card__media catering-photo" role="img" aria-label="Photo of a catering buffet with chafing dishes of food"></div>
    <p class="card__text" style="top:212px;">Lorem Ipsum is simply dummy text of the printing and typesetting industry. Lorem Ipsum has been the industry's standard dummy text ever since the 1500s, when an unknown printer took a galley of type and scrambled it to make &nbsp;...</p>
    <span class="card__link" style="top:360px; left:20px;">Read More &nbsp;&gt;&gt;</span>
  </article>

  <footer class="abs footer">
    <div class="abs footer__links">
      <span>Home</span><span class="sep">|</span>
      <span>Event Planning</span><span class="sep">|</span>
      <span>Catering</span><span class="sep">|</span>
      <span>Galleries</span><span class="sep">|</span>
      <span>Venues</span><span class="sep">|</span>
      <span>Contact Us</span>
    </div>
    <div class="abs footer__legal">
      <span>©2013 Company Name , All Rights Reserved</span><span class="sep">|</span>
      <span>Privacy Policy</span><span class="sep">|</span>
      <span>Terms &amp; Conditions</span>
    </div>
    <div class="abs partner"><span class="partner__dot"></span>Bramblecove Events</div>
    <div class="abs social">
      <span class="social__item social__item--a" aria-label="Social profile"></span>
      <span class="social__item social__item--b" aria-label="News feed"></span>
      <span class="social__item social__item--c" aria-label="Social profile"></span>
      <span class="social__item social__item--d" aria-label="Video channel"></span>
    </div>
  </footer>

</body>
</html>
```